Harborlight Vitality Studio Business Cards and Stationary
Harborlight Vitality Studio
Harborlight Vitality Studio Business Cards and Stationary - Massage Therapy
Creative Brief
Use same font as used in my logo
Similar font as in the word Foundation, or whatever you feel is appropriate
Professional
Dr. Raymond Okafor, D.C.
Every Step Starts With Balance
none at the moment
877 Go Align (462-5446)
www.frontdesk@harborlightvitalitystudio.com
www.harborlightvitalitystudio.com
1.I would like my Logo on top 2. Every Step Starts With Balance 3. Dr. Raymond Okafor, D.C. 4. 877 Go Align (462-5446) 5.email the web site

```html
<!DOCTYPE html>
<html lang="en">
<head>
<meta charset="utf-8">
<title>Harborlight Vitality Studio Business Card</title>
<link rel="stylesheet" href="https://fonts.googleapis.com/css2?family=Raleway:wght@700&family=Open+Sans:wght@400;600&display=swap">
<style>
  :root {
    --page: #e9eaec;
    --card: #ffffff;
    --brand-blue: #2f7fbf;
    --light-blue: #5a9fd4;
    --deep-blue: #1f5f9c;
    --accent-red: #c8262c;
    --ink: #3a3f46;
    --white: #ffffff;
  }
  * { margin: 0; padding: 0; box-sizing: border-box; }
  html, body {
    width: 1200px; height: 864px; overflow: hidden;
    background: var(--page);
    font-family: "Open Sans", sans-serif;
  }
  .canvas {
    position: relative; width: 1200px; height: 864px;
    display: flex; align-items: center; justify-content: center; gap: 40px;
  }
  .card {
    position: relative; width: 540px; height: 310px;
    background: var(--card); border-radius: 16px; overflow: hidden;
    box-shadow: 0 6px 18px rgba(0,0,0,.12);
  }
  .mark-dot { border-radius: 50%; background: var(--brand-blue); flex: none; }
  .brand-name {
    font-family: "Raleway", sans-serif; font-weight: 700;
    color: var(--brand-blue); line-height: 1.1; letter-spacing: .5px;
  }
  /* front */
  .front-mark {
    position: absolute; left: 50%; top: 50%; transform: translate(-50%, -50%);
    display: flex; align-items: center; gap: 12px;
  }
  .front-mark .mark-dot { width: 34px; height: 34px; }
  .front-mark .brand-name { font-size: 26px; }
  .front-web {
    position: absolute; left: 22px; bottom: 40px;
    transform-origin: left bottom; transform: rotate(-90deg) translate(0, 12px);
    font-size: 11px; letter-spacing: 2.4px; color: var(--ink); white-space: nowrap;
  }
  /* back */
  .back-art { position: absolute; inset: 0; }
  .back-mark {
    position: absolute; left: 22px; top: 146px;
    display: flex; align-items: center; gap: 8px;
  }
  .back-mark .mark-dot { width: 22px; height: 22px; }
  .back-mark .brand-name { font-size: 18px; }
  .person {
    position: absolute; left: 22px; bottom: 12px; color: var(--white);
  }
  .person-name { font-size: 12px; font-weight: 600; line-height: 1.3; }
  .tagline { font-size: 10px; opacity: .9; line-height: 1.3; }
  .contact {
    position: absolute; left: 318px; top: 128px; list-style: none;
    color: var(--white); font-size: 8px;
  }
  .contact li { display: flex; align-items: center; gap: 6px; margin-bottom: 5px; white-space: nowrap; }
  .contact svg { width: 11px; height: 11px; flex: none; }
</style>
</head>
<body>
<main class="canvas">
  <section class="card card-front">
    <div class="front-mark">
      <span class="mark-dot"></span>
      <span class="brand-name">Harborlight<br>Vitality Studio</span>
    </div>
    <p class="front-web">www.harborlightvitalitystudio.com</p>
  </section>

  <section class="card card-back">
    <svg class="back-art" viewBox="0 0 540 310" preserveAspectRatio="none">
      <path d="M215,0 C315,40 335,120 275,190 C215,245 100,258 0,262 L0,310 L540,310 L540,0 Z" fill="var(--light-blue)"/>
      <path d="M232,0 C332,40 352,124 290,196 C228,254 110,268 0,272 L0,310 L540,310 L540,0 Z" fill="var(--brand-blue)"/>
      <path d="M215,0 C315,40 335,120 275,190 C215,245 100,258 0,262" fill="none" stroke="var(--white)" stroke-width="3" transform="translate(-5,-3)"/>
      <path d="M215,0 C315,40 335,120 275,190 C215,245 100,258 0,262" fill="none" stroke="var(--accent-red)" stroke-width="5" transform="translate(-10,-7)"/>
      <path d="M215,0 C315,40 335,120 275,190 C215,245 100,258 0,262" fill="none" stroke="var(--accent-red)" stroke-width="2" transform="translate(-18,-13)"/>
    </svg>
    <div class="back-mark">
      <span class="mark-dot"></span>
      <span class="brand-name">Harborlight<br>Vitality Studio</span>
    </div>
    <ul class="contact">
      <li>
        <svg viewBox="0 0 12 12"><circle cx="6" cy="6" r="6" fill="var(--white)"/><path d="M4 3.2l1.1 1.4-.6.8a4 4 0 0 0 2.1 2.1l.8-.6L8.8 8 8 9A5 5 0 0 1 3 4z" fill="var(--brand-blue)"/></svg>
        877 Go Align (462-5446)
      </li>
      <li>
        <svg viewBox="0 0 12 12"><circle cx="6" cy="6" r="6" fill="var(--white)"/><rect x="3" y="4" width="6" height="4" fill="none" stroke="var(--brand-blue)"/><path d="M3 4l3 2 3-2" fill="none" stroke="var(--brand-blue)"/></svg>
        www.frontdesk@harborlightvitalitystudio.com
      </li>
      <li>
        <svg viewBox="0 0 12 12"><circle cx="6" cy="6" r="6" fill="var(--white)"/><circle cx="6" cy="6" r="3" fill="none" stroke="var(--brand-blue)"/><path d="M3 6h6M6 3v6" stroke="var(--brand-blue)"/></svg>
        www.harborlightvitalitystudio.com
      </li>
    </ul>
    <div class="person">
      <p class="person-name">Dr. Raymond Okafor, D.C.</p>
      <p class="tagline">Every Step Starts With Balance</p>
    </div>
  </section>
</main>
</body>
</html>
```